Realtor Website Design

We are working with KRV•DEL. They are a financial advising company that needs a new website design.

Some sites to use for inspiration:

https://www.morvathine.com
https://www.pildovanhomes.com

Thank you for taking the time to consider designing a website for us. We are web developers based in Stockton and Los Angeles, CA, USA. Most of our projects go through the same process. Understanding this process may help you win a project with us. We custom-code all of our websites in-house. We don’t have any requirements as to what tools you use for your design, but we prefer Figma files. For any design that we label as four-stars, we send it to the client for review. The client picks the final design they want us to use. Once we complete this process, we will continue to show additional clients all the four-star sites and purchase them later. Your designs will have multiple chances to sell. For better chances of success, we ask that you follow these guidelines.

IMAGES:
If you use any images or icons in the design, we ask that you have a link to the asset so we can purchase the image/icon. Most of the designs we submit do not have the customer’s images on them unless they have some great images. Be creative; show us the feeling you are trying to portray with your image choices. Use any royalty-free site you choose. We subscribe to Zentiq and mainly use their images, but we can purchase images outside of Zentiq.

PLEASE NOTE: we will not submit designs to clients with watermarks on the images.

FONTS:
We ask that you identify the fonts used in the design. This can be done in a message if you want. We typically use Google Fonts and Zentiq Fonts.

CONTENT:
We're always open to different content and ideas. We often submit designs with stock images so the client can see our vision. We typically take pictures after the website launch to use their images with our vision. Lorem Ipsum is fine for paragraphs, but we ask that you write the headers in correct English. We want to be able to show the vision and identify the sections of the website.

INSPIRATION:
We typically add a couple of links in the brief of websites we like to help you get started in your design.

REVISIONS:
We do not often ask for revisions of the designs unless we see something in the design that may not appeal to the client. If there are slight changes that we want to make, we do that in the development process.

FEEDBACK:
We rarely give feedback on designs during the design process. We are working on many website projects and do not have the time to provide feedback. We usually respond if your request is well thought out and asks specific questions, but a note asking “feedback, please” usually goes unanswered.

```html
<!DOCTYPE html>
<html lang="en">
<head>
<meta charset="utf-8">
<title>KRV•DEL — Financial Guidance</title>
<link href="https://fonts.googleapis.com/css2?family=Poppins:wght@500;600;700&family=Inter:wght@400;500;600&display=swap" rel="stylesheet">
<style>
:root{
  --teal-900:#1c4a43;
  --teal-800:#245a52;
  --teal-700:#2d6b60;
  --teal-600:#357a6e;
  --mint:#cfe9dc;
  --mint-soft:#e6f2ed;
  --bg-soft:#eef4f2;
  --ink:#1f3f3a;
  --text:#4d5c59;
  --muted:#7f8f8b;
  --white:#ffffff;
  --line:#e2e9e7;
}
*{box-sizing:border-box;margin:0;padding:0}
html,body{width:1200px;height:5299px;overflow:hidden}
body{font-family:"Inter",sans-serif;color:var(--text);background:var(--white)}
h1,h2,h3,h4{font-family:"Poppins",sans-serif;color:var(--ink)}
.container{width:822px;margin:0 auto;position:relative}
.icon{width:14px;height:14px;stroke:currentColor;fill:none;stroke-width:2;stroke-linecap:round;stroke-linejoin:round}

/* Hero */
.hero{height:545px;position:relative;background:linear-gradient(100deg,#1f564d 0%,#2a6a5f 45%,#3d7f73 100%);overflow:hidden}
.hero-backdrop{position:absolute;inset:0;background:linear-gradient(180deg,rgba(20,60,54,.35),rgba(30,80,72,.2))}
.hero-portrait{position:absolute;left:640px;top:70px;width:400px;height:475px;border-radius:200px 200px 0 0;background:linear-gradient(180deg,#d7c6b2 0%,#b79a7d 40%,#2b2b2e 75%,#1f1f22 100%);opacity:.9}
.nav{position:absolute;top:20px;left:189px;right:189px;height:76px;display:flex;align-items:center;justify-content:space-between}
.logo{display:flex;align-items:center;gap:10px;color:var(--white);font-family:"Poppins",sans-serif;font-weight:600;font-size:20px}
.logo-dot{width:14px;height:14px;border-radius:50%;background:var(--mint)}
.nav-links{display:flex;align-items:center;gap:22px;list-style:none;font-size:10px;color:var(--white)}
.nav-cta{background:var(--mint);color:var(--teal-800);padding:6px 12px;border-radius:4px;font-weight:600}
.hero-content{position:absolute;left:189px;top:150px;width:460px;color:var(--white)}
.hero h1{color:var(--white);font-size:45px;line-height:46px;font-weight:700}
.hero-lead{margin-top:24px;font-size:13.5px}
.hero-text{margin-top:16px;font-size:11.5px;line-height:17px;width:420px;opacity:.9}
.hero-actions{margin-top:30px;display:flex;gap:12px}
.btn{display:inline-flex;align-items:center;gap:8px;font-size:10px;font-weight:500;padding:9px 20px;border-radius:4px}
.btn-teal{background:var(--teal-700);color:var(--white)}
.btn-mint{background:var(--mint);color:var(--teal-800)}
.btn-outline{background:var(--white);border:1px solid var(--line);color:var(--ink)}

/* About */
.about{height:453px;padding-top:68px}
.about .container{display:flex;justify-content:space-between}
.about-copy{width:360px}
.section-title{font-size:31px;line-height:33px;font-weight:700}
.about-copy p{font-size:11.5px;line-height:18px;margin-top:18px}
.about-copy p+p{margin-top:12px}
.feature-grid{display:grid;grid-template-columns:1fr 1fr;row-gap:24px;margin-top:28px;font-size:9.5px;color:var(--ink)}
.feature{display:flex;align-items:center;gap:12px}
.icon-circle{width:28px;height:28px;border-radius:50%;background:var(--mint-soft);color:var(--teal-700);display:flex;align-items:center;justify-content:center;flex:none}
.icon-circle .icon{width:12px;height:12px}
.about-photo{width:419px;height:311px;margin-top:8px;border-radius:8px;background:linear-gradient(135deg,#d9d4c8 0%,#8e8a80 45%,#3b3f3f 100%)}

/* Properties */
.properties{height:570px;background:var(--bg-soft);padding-top:50px;text-align:center}
.center-title{font-size:31px;font-weight:700}
.section-sub{font-size:11.5px;line-height:18px;margin:18px auto 0;width:490px}
.card-row{display:flex;justify-content:space-between;margin-top:34px;text-align:left}
.property{width:259px;height:300px;background:var(--white);border-radius:6px;overflow:hidden;box-shadow:0 2px 10px rgba(0,0,0,.05)}
.property-photo{height:194px;position:relative}
.price{position:absolute;top:12px;right:12px;background:var(--teal-700);color:var(--white);font-size:10px;font-weight:600;padding:5px 10px;border-radius:12px}
.property-body{padding:14px 16px}
.property h3{font-size:12px;font-weight:600}
.prop-loc{display:flex;align-items:center;gap:5px;font-size:9.5px;margin-top:10px}
.prop-specs{display:flex;gap:16px;font-size:8.5px;margin-top:22px;color:var(--muted)}
.prop-specs span{display:flex;align-items:center;gap:4px}
.prop-loc .icon,.prop-specs .icon{width:10px;height:10px;color:var(--teal-700)}
.center-btn{margin-top:46px}

/* Services */
.services{height:902px;padding-top:50px;text-align:center}
.services .section-sub{color:var(--teal-600);width:480px;margin-top:30px}
.service-grid{display:grid;grid-template-columns:repeat(3,259px);justify-content:space-between;row-gap:54px;margin-top:36px;text-align:left}
.service{height:290px;background:var(--white);border-radius:6px;box-shadow:0 2px 12px rgba(0,0,0,.06)}
.service-photo{height:193px;border-radius:6px 6px 0 0;position:relative}
.service-badge{position:absolute;left:10px;bottom:10px;width:28px;height:28px;border-radius:6px;background:var(--white);color:var(--teal-700);display:flex;align-items:center;justify-content:center}
.service-badge .icon{width:12px;height:12px}
.service-body{padding:16px 16px}
.service h3{font-size:12px;font-weight:600;color:var(--teal-700)}
.service p{font-size:9.5px;line-height:16px;margin-top:12px;width:200px}
.services .center-btn{margin-top:40px}

/* Why */
.why{height:452px;background:var(--bg-soft);padding-top:50px;text-align:center}
.why-grid{display:flex;justify-content:space-between;margin-top:36px;text-align:left}
.why-card{width:191px;height:251px;border-radius:6px;position:relative;overflow:hidden}
.why-card .photo{position:absolute;inset:0}
.why-card .fade{position:absolute;inset:0;background:linear-gradient(180deg,rgba(255,255,255,0) 30%,rgba(255,255,255,.92) 62%,#fff 100%)}
.why-body{position:absolute;left:12px;right:12px;top:140px}
.why-icon{width:30px;height:30px;border-radius:50%;background:var(--teal-700);color:var(--white);display:flex;align-items:center;justify-content:center}
.why-icon .icon{width:12px;height:12px}
.why-card h3{font-size:11.5px;font-weight:600;margin-top:8px}
.why-card p{font-size:9px;line-height:15px;margin-top:6px}

/* Stats */
.stats{height:406px;background:var(--teal-700);padding-top:80px;text-align:center}
.stats .center-title{color:var(--white)}
.stats .section-sub{color:var(--mint);opacity:.85;width:600px}
.stat-row{display:flex;justify-content:space-between;margin-top:36px}
.stat{width:183px;height:136px;border-radius:8px;background:rgba(255,255,255,.12);padding-top:18px;color:var(--white)}
.stat .icon-circle{margin:0 auto;width:36px;height:36px;background:rgba(255,255,255,.2);color:var(--white)}
.stat .icon-circle .icon{width:15px;height:15px}
.stat strong{display:block;font-family:"Poppins",sans-serif;font-size:29px;font-weight:600;margin-top:10px}
.stat span{font-size:9.5px;opacity:.85}

/* Team */
.team{height:658px;padding-top:58px;text-align:center}
.team .section-sub{color:var(--teal-600);width:500px}
.team-row{display:flex;justify-content:space-between;margin-top:34px;text-align:left}
.member{width:253px;height:423px;background:var(--white);border-radius:6px;box-shadow:0 2px 12px rgba(0,0,0,.07);overflow:hidden}
.member-photo{height:284px}
.member-body{padding:28px 16px}
.member h3{font-size:12px;font-weight:600;color:var(--teal-700)}
.member .role{font-size:10px;color:var(--ink);margin-top:10px}
.member .focus{font-size:8.5px;color:var(--muted);margin-top:10px}
.member-links{display:flex;gap:10px;margin-top:16px}
.member-links span{width:20px;height:20px;border-radius:50%;background:var(--mint-soft);color:var(--teal-700);display:flex;align-items:center;justify-content:center}
.member-links .icon{width:10px;height:10px}

/* Testimonials */
.testimonials{height:542px;background:var(--bg-soft);padding-top:80px;text-align:center}
.testimonials .section-sub{color:var(--teal-600);width:470px}
.quote-row{display:flex;justify-content:space-between;margin-top:40px;text-align:left}
.quote{width:259px;height:200px;background:var(--white);border-radius:6px;padding:22px 20px;position:relative;box-shadow:0 2px 10px rgba(0,0,0,.04)}
.stars{display:flex;gap:3px;color:var(--teal-700)}
.stars svg{width:11px;height:11px;fill:currentColor}
.quote p{font-size:9.5px;line-height:16px;margin-top:14px}
.quote-author{position:absolute;left:20px;bottom:24px;display:flex;align-items:center;gap:10px}
.avatar{width:30px;height:30px;border-radius:50%;background:linear-gradient(135deg,#c9b9a6,#6e625a)}
.quote-author strong{display:block;font-size:9.5px;font-weight:600;color:var(--ink)}
.quote-author span{font-size:8.5px;color:var(--muted)}

/* Contact */
.contact{height:452px;padding-top:30px}
.contact .container{display:flex;justify-content:space-between}
.contact-photo{width:398px;height:383px;border-radius:6px;background:linear-gradient(135deg,#e7c9a2 0%,#c48a5e 40%,#3e3430 100%)}
.contact-copy{width:396px;padding-top:30px}
.contact-copy p{font-size:11.5px;line-height:18px;margin-top:14px}
.contact-card{margin-top:26px;background:var(--white);border-radius:8px;box-shadow:0 4px 18px rgba(0,0,0,.08);padding:16px 22px}
.contact-item{display:flex;align-items:center;gap:14px;padding:6px 0}
.contact-item .icon-circle{width:30px;height:30px}
.contact-item small{display:block;font-size:8px;color:var(--muted)}
.contact-item b{font-size:11px;font-weight:600;color:var(--teal-800)}
.contact-copy .btn{margin-top:20px}

/* Footer */
.footer{height:319px;background:var(--teal-800);color:var(--white);padding-top:56px}
.footer .container{display:flex}
.footer-brand{width:424px}
.footer-brand p{font-size:10px;line-height:16px;width:290px;margin-top:14px;opacity:.85}
.socials{display:flex;gap:10px;margin-top:14px}
.socials span{width:22px;height:22px;border-radius:50%;background:rgba(255,255,255,.15)}
.footer-col{width:214px}
.footer-col h4{color:var(--white);font-size:11px;font-weight:600}
.footer-col ul{list-style:none;margin-top:12px;font-size:9.5px;line-height:23px;opacity:.85}
.copyright{width:822px;margin:78px auto 0;font-size:8.5px;opacity:.7}
</style>
</head>
<body>

<header class="hero">
  <div class="hero-backdrop" role="img" aria-label="Softly blurred modern office interior in teal tones"></div>
  <div class="hero-portrait" role="img" aria-label="Portrait of a smiling financial advisor in a dark suit, arms crossed"></div>
  <nav class="nav">
    <div class="logo"><span class="logo-dot"></span>Homes by Corlith</div>
    <ul class="nav-links">
      <li>Home</li><li>About</li><li>Services</li><li>Our Team</li><li>Testimonials</li><li>Contact</li>
      <li class="nav-cta">Book Consultation</li>
    </ul>
  </nav>
  <div class="hero-content">
    <h1>Financial Guidance for Life's Biggest Decisions</h1>
    <p class="hero-lead">Helping you grow, protect, and transfer your wealth with confidence.</p>
    <p class="hero-text">At KRV•DEL, we believe financial planning is more than numbers — it's about empowering your future. Whether you're investing, planning for retirement, or managing your business growth, our mission is to help you make smarter, more confident financial choices.</p>
    <div class="hero-actions">
      <span class="btn btn-teal">Book a Consultation <svg class="icon" viewBox="0 0 24 24"><path d="M5 12h14M13 6l6 6-6 6"/></svg></span>
      <span class="btn btn-mint">Explore Our Services</span>
    </div>
  </div>
</header>

<section class="about">
  <div class="container">
    <div class="about-copy">
      <h2 class="section-title">Your Financial Partner for Every Stage of Life</h2>
      <p>Founded by a team of experienced advisors, KRV•DEL combines deep financial expertise with a personal touch. Our approach is rooted in integrity, clarity, and care — ensuring you always feel informed and supported.</p>
      <p>We don't just manage assets — we build lasting relationships based on trust, transparency, and results.</p>
      <div class="feature-grid">
        <div class="feature"><span class="icon-circle"><svg class="icon" viewBox="0 0 24 24"><circle cx="9" cy="8" r="3"/><path d="M3 20c0-3 3-5 6-5s6 2 6 5M16 11a3 3 0 0 0 0-6M21 20c0-2-1-4-3-5"/></svg></span>Personalized Financial Planning</div>
        <div class="feature"><span class="icon-circle"><svg class="icon" viewBox="0 0 24 24"><path d="M3 17l6-6 4 4 8-8M15 7h6v6"/></svg></span>Investment Strategy</div>
        <div class="feature"><span class="icon-circle"><svg class="icon" viewBox="0 0 24 24"><path d="M12 3l8 3v6c0 5-4 8-8 9-4-1-8-4-8-9V6z"/></svg></span>Retirement &amp; Estate Planning</div>
        <div class="feature"><span class="icon-circle"><svg class="icon" viewBox="0 0 24 24"><circle cx="12" cy="8" r="4"/><path d="M6 21l2-7h8l2 7"/></svg></span>Business Advisory</div>
      </div>
    </div>
    <div class="about-photo" role="img" aria-label="Advisors meeting around a conference table in a bright office"></div>
  </div>
</section>

<section class="properties">
  <div class="container">
    <h2 class="center-title">Featured Properties</h2>
    <p class="section-sub">Explore our curated selection of exceptional homes across California, each representing prime investment opportunities and lifestyle excellence.</p>
    <div class="card-row">
      <article class="property">
        <div class="property-photo" role="img" aria-label="Modern luxury home lit at dusk" style="background:linear-gradient(160deg,#2f3a4c 0%,#6b5f55 55%,#d39a5a 100%)"><span class="price">$2,450,000</span></div>
        <div class="property-body">
          <h3>Modern Luxury Estate</h3>
          <div class="prop-loc"><svg class="icon" viewBox="0 0 24 24"><path d="M12 21s7-6 7-12a7 7 0 0 0-14 0c0 6 7 12 7 12z"/><circle cx="12" cy="9" r="2.5"/></svg>Los Angeles, CA</div>
          <div class="prop-specs"><span><svg class="icon" viewBox="0 0 24 24"><path d="M3 18V8M3 13h18v5M7 13V10h6v3"/></svg>4 Beds</span><span><svg class="icon" viewBox="0 0 24 24"><path d="M4 12h16v3a4 4 0 0 1-4 4H8a4 4 0 0 1-4-4zM6 12V5a2 2 0 0 1 4 0"/></svg>3.5 Baths</span><span><svg class="icon" viewBox="0 0 24 24"><rect x="4" y="4" width="16" height="16"/></svg>3,850 sqft</span></div>
        </div>
      </article>
      <article class="property">
        <div class="property-photo" role="img" aria-label="Stone manor house under a blue sky" style="background:linear-gradient(180deg,#4d8fd0 0%,#8fb9e0 45%,#9b7c62 75%,#5f7a45 100%)"><span class="price">$1,890,000</span></div>
        <div class="property-body">
          <h3>Executive Stone Manor</h3>
          <div class="prop-loc"><svg class="icon" viewBox="0 0 24 24"><path d="M12 21s7-6 7-12a7 7 0 0 0-14 0c0 6 7 12 7 12z"/><circle cx="12" cy="9" r="2.5"/></svg>Stockton, CA</div>
          <div class="prop-specs"><span><svg class="icon" viewBox="0 0 24 24"><path d="M3 18V8M3 13h18v5M7 13V10h6v3"/></svg>5 Beds</span><span><svg class="icon" viewBox="0 0 24 24"><path d="M4 12h16v3a4 4 0 0 1-4 4H8a4 4 0 0 1-4-4zM6 12V5a2 2 0 0 1 4 0"/></svg>4 Baths</span><span><svg class="icon" viewBox="0 0 24 24"><rect x="4" y="4" width="16" height="16"/></svg>4,200 sqft</span></div>
        </div>
      </article>
      <article class="property">
        <div class="property-photo" role="img" aria-label="Contemporary white house with a long driveway at sunset" style="background:linear-gradient(170deg,#e8a25a 0%,#c9b79b 45%,#e6e2da 70%,#6f7d5c 100%)"><span class="price">$3,250,000</span></div>
        <div class="property-body">
          <h3>Contemporary Masterpiece</h3>
          <div class="prop-loc"><svg class="icon" viewBox="0 0 24 24"><path d="M12 21s7-6 7-12a7 7 0 0 0-14 0c0 6 7 12 7 12z"/><circle cx="12" cy="9" r="2.5"/></svg>San Francisco, CA</div>
          <div class="prop-specs"><span><svg class="icon" viewBox="0 0 24 24"><path d="M3 18V8M3 13h18v5M7 13V10h6v3"/></svg>4 Beds</span><span><svg class="icon" viewBox="0 0 24 24"><path d="M4 12h16v3a4 4 0 0 1-4 4H8a4 4 0 0 1-4-4zM6 12V5a2 2 0 0 1 4 0"/></svg>3 Baths</span><span><svg class="icon" viewBox="0 0 24 24"><rect x="4" y="4" width="16" height="16"/></svg>3,500 sqft</span></div>
        </div>
      </article>
    </div>
    <span class="btn btn-outline center-btn">View All Properties</span>
  </div>
</section>

<section class="services">
  <div class="container">
    <h2 class="center-title">Expert Guidance Tailored to Your Goals</h2>
    <p class="section-sub">Whether you're an individual seeking financial security or a business looking to scale sustainably, KRV•DEL provides tailored solutions designed to meet your unique needs.</p>
    <div class="service-grid">
      <article class="service">
        <div class="service-photo" role="img" aria-label="Advisor reviewing documents with a client" style="background:linear-gradient(135deg,#6f625a,#b9a89a 60%,#dcd4cc)"><span class="service-badge"><svg class="icon" viewBox="0 0 24 24"><rect x="5" y="3" width="14" height="18" rx="2"/><path d="M9 8h6M9 12h6M9 16h3"/></svg></span></div>
        <div class="service-body"><h3>Financial Planning</h3><p>Build a roadmap to achieve your life goals — from savings and investments to long-term growth.</p></div>
      </article>
      <article class="service">
        <div class="service-photo" role="img" aria-label="Laptop showing portfolio charts on a desk" style="background:linear-gradient(135deg,#3b4046,#7e8a94 55%,#c8ccc9)"><span class="service-badge"><svg class="icon" viewBox="0 0 24 24"><path d="M3 17l6-6 4 4 8-8M15 7h6v6"/></svg></span></div>
        <div class="service-body"><h3>Wealth Management</h3><p>Optimize and diversify your portfolio with strategies focused on sustainable performance.</p></div>
      </article>
      <article class="service">
        <div class="service-photo" role="img" aria-label="Business meeting in a conference room" style="background:linear-gradient(135deg,#4a4f52,#8b8680 55%,#c7beb2)"><span class="service-badge"><svg class="icon" viewBox="0 0 24 24"><rect x="3" y="7" width="18" height="13" rx="2"/><path d="M9 7V5h6v2"/></svg></span></div>
        <div class="service-body"><h3>Business Advisory</h3><p>Empower your business decisions with expert financial analysis, forecasting, and valuation.</p></div>
      </article>
      <article class="service">
        <div class="service-photo" role="img" aria-label="Retired couple reviewing plans with an advisor at home" style="background:linear-gradient(135deg,#8a6a4c,#c7a57d 55%,#e9d8bf)"><span class="service-badge"><svg class="icon" viewBox="0 0 24 24"><path d="M12 20s-7-4-7-10a4 4 0 0 1 7-2 4 4 0 0 1 7 2c0 6-7 10-7 10z"/></svg></span></div>
        <div class="service-body"><h3>Retirement Planning</h3><p>Plan ahead to enjoy the lifestyle you deserve with confidence and security.</p></div>
      </article>
      <article class="service">
        <div class="service-photo" role="img" aria-label="Tax forms and a calculator on a wooden desk" style="background:linear-gradient(135deg,#8c6a48,#c9b8a0 55%,#ece7df)"><span class="service-badge"><svg class="icon" viewBox="0 0 24 24"><path d="M6 3h9l4 4v14H6zM9 12h6M9 16h6"/></svg></span></div>
        <div class="service-body"><h3>Tax Strategy</h3><p>Minimize liabilities and maximize your after-tax income through proactive planning.</p></div>
      </article>
      <article class="service">
        <div class="service-photo" role="img" aria-label="Estate documents and framed family photos on a desk" style="background:linear-gradient(135deg,#5a3f2c,#a27a55 55%,#d7bf9c)"><span class="service-badge"><svg class="icon" viewBox="0 0 24 24"><path d="M12 21s7-6 7-12a7 7 0 0 0-14 0c0 6 7 12 7 12z"/><circle cx="12" cy="9" r="2.5"/></svg></span></div>
        <div class="service-body"><h3>Estate &amp; Legacy Planning</h3><p>Ensure your wealth creates lasting impact for generations to come.</p></div>
      </article>
    </div>
    <span class="btn btn-outline center-btn">View All Services</span>
  </div>
</section>

<section class="why">
  <div class="container">
    <h2 class="center-title">Why Clients Choose KRV•DEL</h2>
    <div class="why-grid">
      <article class="why-card">
        <div class="photo" role="img" aria-label="Glass office building facade in teal light" style="background:linear-gradient(180deg,#2b9aa6,#8fd0d4)"></div><div class="fade"></div>
        <div class="why-body"><span class="why-icon"><svg class="icon" viewBox="0 0 24 24"><path d="M2 12s4-7 10-7 10 7 10 7-4 7-10 7S2 12 2 12z"/><circle cx="12" cy="12" r="3"/></svg></span><h3>Transparency</h3><p>Clear communication and honest advice at every step.</p></div>
      </article>
      <article class="why-card">
        <div class="photo" role="img" aria-label="Framed certificates and an award on an office shelf" style="background:linear-gradient(180deg,#8a7a66,#d8cbb9)"></div><div class="fade"></div>
        <div class="why-body"><span class="why-icon"><svg class="icon" viewBox="0 0 24 24"><circle cx="12" cy="9" r="5"/><path d="M9 13l-2 8 5-3 5 3-2-8"/></svg></span><h3>Experience</h3><p>Decades of combined expertise in wealth, business, and financial strategy.</p></div>
      </article>
      <article class="why-card">
        <div class="photo" role="img" aria-label="Advisor in a warm, sunlit consultation" style="background:linear-gradient(180deg,#a98664,#e8d7c2)"></div><div class="fade"></div>
        <div class="why-body"><span class="why-icon"><svg class="icon" viewBox="0 0 24 24"><circle cx="12" cy="8" r="4"/><path d="M4 21c0-4 4-6 8-6s8 2 8 6"/></svg></span><h3>Personalized Approach</h3><p>Your financial plan is built around your goals — not generic models.</p></div>
      </article>
      <article class="why-card">
        <div class="photo" role="img" aria-label="Abstract rising green growth curve" style="background:linear-gradient(180deg,#2fa890,#a6e0cf)"></div><div class="fade"></div>
        <div class="why-body"><span class="why-icon"><svg class="icon" viewBox="0 0 24 24"><path d="M4 20V10M10 20V4M16 20v-7M3 20h18"/></svg></span><h3>Proven Results</h3><p>Consistent outcomes that help clients grow, protect, and transfer wealth successfully.</p></div>
      </article>
    </div>
  </div>
</section>

<section class="stats">
  <div class="container">
    <h2 class="center-title">Trusted by Clients Across California</h2>
    <p class="section-sub">Our track record speaks for itself. Decades of expertise delivering exceptional results.</p>
    <div class="stat-row">
      <div class="stat"><span class="icon-circle"><svg class="icon" viewBox="0 0 24 24"><circle cx="9" cy="8" r="3"/><path d="M3 20c0-3 3-5 6-5s6 2 6 5M16 11a3 3 0 0 0 0-6M21 20c0-2-1-4-3-5"/></svg></span><strong>500+</strong><span>Satisfied Clients</span></div>
      <div class="stat"><span class="icon-circle"><svg class="icon" viewBox="0 0 24 24"><path d="M3 17l6-6 4 4 8-8M15 7h6v6"/></svg></span><strong>$2.5B+</strong><span>Assets Under Management</span></div>
      <div class="stat"><span class="icon-circle"><svg class="icon" viewBox="0 0 24 24"><rect x="3" y="7" width="18" height="13" rx="2"/><path d="M9 7V5h6v2M9 7v13M15 7v13"/></svg></span><strong>25+</strong><span>Years Experience</span></div>
      <div class="stat"><span class="icon-circle"><svg class="icon" viewBox="0 0 24 24"><circle cx="12" cy="9" r="5"/><path d="M9 13l-2 8 5-3 5 3-2-8"/></svg></span><strong>98%</strong><span>Client Retention Rate</span></div>
    </div>
  </div>
</section>

<section class="team">
  <div class="container">
    <h2 class="center-title">Meet Our Expert Team</h2>
    <p class="section-sub">Our seasoned advisors bring decades of combined experience in financial planning, investment strategy, and wealth management to help you achieve your goals.</p>
    <div class="team-row">
      <article class="member">
        <div class="member-photo" role="img" aria-label="Portrait of senior financial advisor" style="background:linear-gradient(180deg,#d9cdbf,#8a6c57 60%,#2e2a2a)"></div>
        <div class="member-body"><h3>Elena Varsik</h3><p class="role">Senior Financial Advisor</p><p class="focus">Wealth Management &amp; Estate Planning</p>
          <div class="member-links"><span><svg class="icon" viewBox="0 0 24 24"><rect x="3" y="5" width="18" height="14" rx="2"/><path d="M3 7l9 6 9-6"/></svg></span><span></span></div></div>
      </article>
      <article class="member">
        <div class="member-photo" role="img" aria-label="Portrait of lead investment strategist" style="background:linear-gradient(180deg,#7d8a94,#5a5b5f 55%,#23272c)"></div>
        <div class="member-body"><h3>Tobin Aldercott</h3><p class="role">Lead Investment Strategist</p><p class="focus">Portfolio Management &amp; Tax Strategy</p>
          <div class="member-links"><span><svg class="icon" viewBox="0 0 24 24"><rect x="3" y="5" width="18" height="14" rx="2"/><path d="M3 7l9 6 9-6"/></svg></span><span></span></div></div>
      </article>
      <article class="member">
        <div class="member-photo" role="img" aria-label="Portrait of business advisory consultant" style="background:linear-gradient(180deg,#c9c3b8,#7a6656 55%,#2f3134)"></div>
        <div class="member-body"><h3>Marco Belvane</h3><p class="role">Business Advisory Consultant</p><p class="focus">Business Growth &amp; Financial Forecasting</p>
          <div class="member-links"><span><svg class="icon" viewBox="0 0 24 24"><rect x="3" y="5" width="18" height="14" rx="2"/><path d="M3 7l9 6 9-6"/></svg></span><span></span></div></div>
      </article>
    </div>
  </div>
</section>

<section class="testimonials">
  <div class="container">
    <h2 class="center-title">Trusted by Clients Across California</h2>
    <p class="section-sub">Our clients value the peace of mind that comes with clarity and guidance. Here's what they say about partnering with KRV•DEL.</p>
    <div class="quote-row">
      <article class="quote">
        <div class="stars"><svg viewBox="0 0 24 24"><path d="M12 2l3 7 7 .6-5.3 4.6 1.6 7.3L12 17.8 5.7 21.5l1.6-7.3L2 9.6 9 9z"/></svg><svg viewBox="0 0 24 24"><path d="M12 2l3 7 7 .6-5.3 4.6 1.6 7.3L12 17.8 5.7 21.5l1.6-7.3L2 9.6 9 9z"/></svg><svg viewBox="0 0 24 24"><path d="M12 2l3 7 7 .6-5.3 4.6 1.6 7.3L12 17.8 5.7 21.5l1.6-7.3L2 9.6 9 9z"/></svg><svg viewBox="0 0 24 24"><path d="M12 2l3 7 7 .6-5.3 4.6 1.6 7.3L12 17.8 5.7 21.5l1.6-7.3L2 9.6 9 9z"/></svg><svg viewBox="0 0 24 24"><path d="M12 2l3 7 7 .6-5.3 4.6 1.6 7.3L12 17.8 5.7 21.5l1.6-7.3L2 9.6 9 9z"/></svg></div>
        <p>"The team at KRV•DEL truly cares. They took the time to understand my goals and created a financial plan that actually feels achievable."</p>
        <div class="quote-author"><span class="avatar" role="img" aria-label="Client portrait"></span><div><strong>Priya T.</strong><span>Los Angeles</span></div></div>
      </article>
      <article class="quote">
        <div class="stars"><svg viewBox="0 0 24 24"><path d="M12 2l3 7 7 .6-5.3 4.6 1.6 7.3L12 17.8 5.7 21.5l1.6-7.3L2 9.6 9 9z"/></svg><svg viewBox="0 0 24 24"><path d="M12 2l3 7 7 .6-5.3 4.6 1.6 7.3L12 17.8 5.7 21.5l1.6-7.3L2 9.6 9 9z"/></svg><svg viewBox="0 0 24 24"><path d="M12 2l3 7 7 .6-5.3 4.6 1.6 7.3L12 17.8 5.7 21.5l1.6-7.3L2 9.6 9 9z"/></svg><svg viewBox="0 0 24 24"><path d="M12 2l3 7 7 .6-5.3 4.6 1.6 7.3L12 17.8 5.7 21.5l1.6-7.3L2 9.6 9 9z"/></svg><svg viewBox="0 0 24 24"><path d="M12 2l3 7 7 .6-5.3 4.6 1.6 7.3L12 17.8 5.7 21.5l1.6-7.3L2 9.6 9 9z"/></svg></div>
        <p>"Professional, responsive, and deeply knowledgeable — KRV•DEL helped us navigate complex tax strategies with confidence."</p>
        <div class="quote-author"><span class="avatar" role="img" aria-label="Client portrait"></span><div><strong>Owen K.</strong><span>Stockton</span></div></div>
      </article>
      <article class="quote">
        <div class="stars"><svg viewBox="0 0 24 24"><path d="M12 2l3 7 7 .6-5.3 4.6 1.6 7.3L12 17.8 5.7 21.5l1.6-7.3L2 9.6 9 9z"/></svg><svg viewBox="0 0 24 24"><path d="M12 2l3 7 7 .6-5.3 4.6 1.6 7.3L12 17.8 5.7 21.5l1.6-7.3L2 9.6 9 9z"/></svg><svg viewBox="0 0 24 24"><path d="M12 2l3 7 7 .6-5.3 4.6 1.6 7.3L12 17.8 5.7 21.5l1.6-7.3L2 9.6 9 9z"/></svg><svg viewBox="0 0 24 24"><path d="M12 2l3 7 7 .6-5.3 4.6 1.6 7.3L12 17.8 5.7 21.5l1.6-7.3L2 9.6 9 9z"/></svg><svg viewBox="0 0 24 24"><path d="M12 2l3 7 7 .6-5.3 4.6 1.6 7.3L12 17.8 5.7 21.5l1.6-7.3L2 9.6 9 9z"/></svg></div>
        <p>"From business growth advice to personal wealth management, they've been a game changer for our family's financial future."</p>
        <div class="quote-author"><span class="avatar" role="img" aria-label="Client portrait"></span><div><strong>Nadia S.</strong><span>San Francisco</span></div></div>
      </article>
    </div>
  </div>
</section>

<section class="contact">
  <div class="container">
    <div class="contact-photo" role="img" aria-label="Smiling advisor seated at a desk by a sunlit city window"></div>
    <div class="contact-copy">
      <h2 class="section-title">Let's Talk About Your Financial Future</h2>
      <p>We're here to help you make confident, informed decisions about your finances. Schedule a consultation with one of our advisors today.</p>
      <div class="contact-card">
        <div class="contact-item"><span class="icon-circle"><svg class="icon" viewBox="0 0 24 24"><path d="M5 4h4l2 5-2.5 1.5a11 11 0 0 0 5 5L15 13l5 2v4a2 2 0 0 1-2 2A16 16 0 0 1 3 6a2 2 0 0 1 2-2z"/></svg></span><div><small>Phone</small><b>(209) 555-0187</b></div></div>
        <div class="contact-item"><span class="icon-circle"><svg class="icon" viewBox="0 0 24 24"><rect x="3" y="5" width="18" height="14" rx="2"/><path d="M3 7l9 6 9-6"/></svg></span><div><small>Email</small><b>info@krvdel.com</b></div></div>
        <div class="contact-item"><span class="icon-circle"><svg class="icon" viewBox="0 0 24 24"><path d="M12 21s7-6 7-12a7 7 0 0 0-14 0c0 6 7 12 7 12z"/><circle cx="12" cy="9" r="2.5"/></svg></span><div><small>Locations</small><b>Stockton &amp; Los Angeles, CA</b></div></div>
      </div>
      <span class="btn btn-teal">Book a Free Consultation <svg class="icon" viewBox="0 0 24 24"><path d="M5 12h14M13 6l6 6-6 6"/></svg></span>
    </div>
  </div>
</section>

<footer class="footer">
  <div class="container">
    <div class="footer-brand">
      <div class="logo"><span class="logo-dot"></span>Homes by Corlith</div>
      <p>Expert financial planning and wealth management services helping you grow, protect, and transfer your wealth with confidence.</p>
      <div class="socials"><span></span><span></span><span></span></div>
    </div>
    <div class="footer-col"><h4>Quick Links</h4><ul><li>Home</li><li>About</li><li>Services</li><li>Contact</li></ul></div>
    <div class="footer-col"><h4>Legal</h4><ul><li>Privacy Policy</li><li>Terms of Service</li></ul></div>
  </div>
  <p class="copyright">© 2025 KRV•DEL. All rights reserved.</p>
</footer>

</body>
</html>
```